Masonry and Landscaping Construction company business card

Looking for a business card design for a construction company named Ferrano Construction. It is an italian-american family business that specializes in custom stone work, patios, walkways, driveways, steps, outdoor kitchens, concrete, waterproofing, power wash, landscaping and more. Our colors are mostly red and white with some black. We're looking for a bold design. we also like to incorporate a picture of my family's hometown somewhere in it.
Target Market(s)
Luxury home owners
Industry/Entity Type
Construction
Contact Information for Business Card
Details includes should be bullet points mentioning the services provided. Custom Stone Work, Outdoor Kitchens, Fire Pits, Patios, Walkways, Steps, Concrete, Waterproofing, powerwash and landscaping
Requirements
Must have
- Would like a spot on the card for co-owners names, numbers and email to be listed also looking to add the QR code for an instagram page
Nice to have
- would like something bold, based around the colors red and white with black outlines or details

```html
<!DOCTYPE html>
<html lang="en">
<head>
<meta charset="utf-8">
<title>Ferrano Construction Business Card</title>
<link rel="stylesheet" href="https://fonts.googleapis.com/css2?family=Rajdhani:wght@500;600;700&family=Roboto:wght@400;500&display=swap">
<style>
  :root {
    --backdrop: #3a3a3c;
    --card-white: #ffffff;
    --brand-red: #d0101f;
    --band-green: #10d15e;
    --ink: #1b1b1b;
    --text-on-grey: #ffffff;
  }
  * { box-sizing: border-box; margin: 0; padding: 0; }
  html, body { width: 1200px; height: 689px; overflow: hidden; }
  body {
    background: var(--backdrop);
    position: relative;
    font-family: "Roboto", Arial, sans-serif;
  }
  .card {
    position: absolute;
    top: 190px;
    width: 540px;
    height: 309px;
    border-radius: 22px;
    overflow: hidden;
    box-shadow: 0 14px 30px rgba(0,0,0,.35);
  }
  /* Front */
  .card-front { left: 40px; }
  .hometown-photo {
    position: absolute; inset: 0;
    background: linear-gradient(180deg, #c9d3db 0%, #a9b8a4 28%, #6f8a5c 55%, #8c7b66 78%, #5f6e48 100%);
  }
  .front-brand {
    position: absolute;
    top: 34px; right: 34px;
    display: flex; align-items: center; gap: 10px;
    font-family: "Rajdhani", sans-serif;
    font-weight: 700;
    font-size: 27px;
    line-height: 1;
    color: var(--card-white);
    text-transform: uppercase;
  }
  .brand-mark {
    width: 18px; height: 18px; border-radius: 50%;
    background: var(--brand-red);
    flex: none;
  }
  .services-band {
    position: absolute;
    left: 0; right: 0; bottom: 34px;
    height: 66px;
    background: var(--band-green);
    display: flex; flex-direction: column; justify-content: center; align-items: center;
    gap: 2px;
    font-family: "Rajdhani", sans-serif;
    font-weight: 600;
    font-size: 17px;
    color: var(--ink);
  }
  .service-row { display: flex; gap: 8px; align-items: center; }
  .service-row .dot {
    width: 6px; height: 6px; border-radius: 50%; background: var(--brand-red);
  }
  /* Back */
  .card-back { left: 620px; background: var(--card-white); }
  .back-shapes { position: absolute; inset: 0; }
  .back-brand {
    position: absolute;
    left: 56px; top: 126px;
    display: flex; align-items: center; gap: 10px;
    font-family: "Rajdhani", sans-serif;
    font-weight: 700;
    font-size: 24px;
    line-height: 1.05;
    color: var(--ink);
    text-transform: uppercase;
  }
  .person {
    position: absolute; top: 20px; right: 30px; text-align: right;
  }
  .person-name {
    font-family: "Rajdhani", sans-serif;
    font-weight: 700; font-size: 24px; line-height: 1;
    color: var(--brand-red);
    text-transform: uppercase;
  }
  .person-role { font-size: 11px; color: var(--ink); margin-top: 2px; }
  .contact-list {
    position: absolute; right: 12px; top: 136px;
    list-style: none; text-align: right;
    color: var(--text-on-grey);
    font-size: 11.5px; line-height: 17px;
  }
  .contact-list li { display: flex; justify-content: flex-end; align-items: center; gap: 8px; }
  .contact-list svg { width: 11px; height: 11px; fill: var(--brand-red); flex: none; }
  .address {
    position: absolute; right: 31px; top: 222px;
    text-align: right; color: var(--text-on-grey);
    font-size: 13px; line-height: 17px;
  }
</style>
</head>
<body>
  <section class="card card-front">
    <div class="hometown-photo" role="img" aria-label="Photograph of the family's Italian hometown: stone church bell tower and houses on a green hillside under a cloudy sky"></div>
    <div class="front-brand"><span class="brand-mark"></span>Ferrano Construction</div>
    <div class="services-band">
      <div class="service-row">
        <span>Custom Stone Work</span><span class="dot"></span>
        <span>Outdoor Kitchens</span><span class="dot"></span>
        <span>Fire Pits</span><span class="dot"></span>
        <span>Patios</span><span class="dot"></span>
        <span>Walkways</span>
      </div>
      <div class="service-row">
        <span>Steps</span><span class="dot"></span>
        <span>Concrete</span><span class="dot"></span>
        <span>Waterproofing</span><span class="dot"></span>
        <span>Powerwash &amp; Landscaping</span>
      </div>
    </div>
  </section>

  <section class="card card-back">
    <svg class="back-shapes" viewBox="0 0 540 309" preserveAspectRatio="none" aria-hidden="true">
      <defs>
        <linearGradient id="grey-panel" x1="0" y1="1" x2="1" y2="0">
          <stop offset="0" stop-color="#5a5a5c"/>
          <stop offset="1" stop-color="#9a9a9c"/>
        </linearGradient>
      </defs>
      <polygon points="0,262 90,300 540,62 540,309 0,309" fill="url(#grey-panel)"/>
      <polyline points="0,262 90,300 540,62" fill="none" stroke="var(--brand-red)" stroke-width="5"/>
    </svg>

    <div class="person">
      <div class="person-name">Marco Bellini</div>
      <div class="person-role">President</div>
    </div>

    <div class="back-brand"><span class="brand-mark"></span>Ferrano<br>Construction</div>

    <ul class="contact-list">
      <li>555-214-7730
        <svg viewBox="0 0 12 12"><path d="M2.5 1h2l1 3-1.3 1a6 6 0 0 0 2.8 2.8L8 6.5l3 1v2A1.5 1.5 0 0 1 9.5 11 8.5 8.5 0 0 1 1 2.5 1.5 1.5 0 0 1 2.5 1z"/></svg></li>
      <li>555-386-1942
        <svg viewBox="0 0 12 12"><path d="M3 0h6a1 1 0 0 1 1 1v10a1 1 0 0 1-1 1H3a1 1 0 0 1-1-1V1a1 1 0 0 1 1-1zm0 1.5v7.5h6V1.5z"/></svg></li>
      <li>info@ferranoconstruction.com
        <svg viewBox="0 0 12 12"><path d="M0 2h12v8H0zm1 1v.4l5 3.2 5-3.2V3z"/></svg></li>
      <li>www.ferranoconstruction.com
        <svg viewBox="0 0 12 12"><circle cx="6" cy="6" r="5.5"/></svg></li>
    </ul>

    <div class="address">412 Alder Court<br>Westfield, Canada 20418</div>
  </section>
</body>
</html>
```